Marrowgate Concepts/Innovation Consultant-One Page (for now) Site Reflective Of Its Focus.

Based in Tampa, Florida...I offer my consulting services, along with my extensive network of companies and technologies, to people that are looking for new, novel, and innovative applications for their technology and/or companies & governmental agencies to identify solutions to their Existing Challenges and Future Needs. I then Identify Connections and/or Solutions between technologies and set up collaborations between the parties. I also run a Forum that allows people to present new, novel, and innovative technologies and capabilities to a broad audience for ideation and collaboration.

Logo Text

Marrowgate Concepts LLC

Coding

```html
<!DOCTYPE html>
<html lang="en">
<head>
<meta charset="utf-8">
<title>Marrowgate Concepts LLC</title>
<link href="https://fonts.googleapis.com/css2?family=Poppins:wght@300;400;500;600&display=swap" rel="stylesheet">
<style>
:root{
  --blue:#0a6cc2;
  --blue-dark:#0b4f8f;
  --ink:#1b1b1b;
  --text:#444;
  --muted:#6b6b6b;
  --pale:#f2f7fd;
  --grey:#f4f4f4;
  --line:#d9dde3;
  --star:#f7931e;
  --white:#fff;
}
*{box-sizing:border-box;margin:0;padding:0}
html,body{width:1200px;height:4739px;overflow:hidden}
body{position:relative;font-family:'Poppins',sans-serif;color:var(--ink);background:var(--white)}
.abs{position:absolute}
section,header,footer{position:absolute;left:0;width:1200px;overflow:hidden}
.eyebrow{font-size:20px;font-weight:500;color:var(--ink);text-align:center}
.title{font-size:42px;font-weight:400;color:var(--blue);text-align:center;line-height:1.15}
.btn{position:absolute;background:var(--blue);color:var(--white);border-radius:8px;font-size:15px;font-weight:500;display:flex;align-items:center;justify-content:center}
.placeholder{position:absolute}

/* hero */
.hero{top:0;height:677px;background:var(--pale)}
.brand-badge{left:86px;top:5px;width:146px;height:146px;border-radius:50%;background:var(--white);display:flex;align-items:center;justify-content:center;text-align:center;font-size:15px;font-weight:600;color:var(--blue);line-height:1.3;padding:16px}
.nav{position:absolute;top:58px;left:527px;display:flex;gap:38px;font-size:15px;color:var(--ink)}
.nav .active{color:var(--blue);position:relative}
.nav .active::after{content:"";position:absolute;left:0;right:0;top:34px;height:2px;background:var(--blue)}
.nav-cta{left:951px;top:42px;width:143px;height:53px;border:1.5px solid var(--blue-dark);border-radius:8px;font-size:15px;display:flex;align-items:center;justify-content:center;color:var(--ink)}
.hero-welcome{left:87px;top:254px;font-size:21px;font-weight:500}
.hero-title{left:86px;top:282px;font-size:55px;font-weight:500;color:var(--blue);line-height:1.1}

/* about */
.about{top:677px;height:652px;background:var(--white)}
.about-copy{left:604px;top:223px;width:505px;font-size:15px;line-height:31px;text-align:justify;color:var(--ink)}

/* services */
.services{top:1329px;height:988px;background:var(--pale)}
.svc{position:absolute;width:350px;text-align:center}
.svc-icon{width:92px;height:86px;margin:0 auto;background:var(--white);border:1px solid var(--line);display:flex;align-items:center;justify-content:center}
.svc h3{font-size:21px;font-weight:500;color:var(--blue);margin-top:25px}
.svc p{font-size:15px;line-height:26px;color:var(--muted);margin:14px auto 0;width:282px;text-align:justify;text-align-last:center}

/* why */
.why{top:2317px;height:486px;background:var(--pale)}
.why-lead{left:0;width:1200px;top:166px;font-size:15px;line-height:26px;text-align:center;color:var(--muted)}
.why-item{position:absolute;top:265px;width:180px;text-align:center}
.why-box{width:103px;height:100px;margin:0 auto;border:1.5px solid var(--blue);padding:6px}
.why-box div{width:100%;height:100%;background:var(--blue);display:flex;align-items:center;justify-content:center}
.why-item span{display:block;margin-top:24px;font-size:15px;color:var(--blue-dark);font-weight:500}

/* testimonials */
.testimonials{top:2803px;height:821px;background:var(--white)}
.t-lead{left:290px;width:620px;top:234px;font-size:15px;line-height:26px;text-align:center;color:var(--muted)}
.t-card{position:absolute;top:396px;width:332px;height:239px;border:2px solid var(--line);border-top:4px solid var(--blue);border-radius:14px;background:var(--white);padding:72px 34px 0;text-align:center;font-size:15px;line-height:26px;color:var(--muted)}
.avatar{position:absolute;top:-43px;left:125px;width:82px;height:82px;border-radius:50%;background:linear-gradient(#c7ccd3,#8a9099);border:3px solid var(--white)}
.t-meta{position:absolute;top:663px;width:332px;text-align:center}
.t-meta b{display:block;font-size:16px;font-weight:600;color:var(--ink)}
.t-meta small{display:block;font-size:13px;color:var(--muted)}
.stars{display:flex;justify-content:center;gap:3px;margin-top:6px}

/* contact */
.contact{top:3624px;height:725px;background:var(--grey)}
.field{position:absolute;background:var(--white);border:1px solid #e4e4e4;border-radius:10px;display:flex;align-items:center;padding-left:30px;gap:18px;font-size:16px;color:#555}
.field.msg{align-items:flex-start;padding-top:28px}

/* footer */
.footer{top:4349px;height:331px;background:var(--pale)}
.f-brand{left:100px;top:100px;width:160px;font-size:22px;font-weight:600;color:var(--blue);line-height:1.25;text-align:center}
.f-col h4{font-size:19px;font-weight:600;color:var(--blue);letter-spacing:.3px}
.f-col ul{list-style:none;margin-top:24px}
.f-col li{font-size:15px;color:var(--ink);line-height:30.5px}
.f-col li::before{content:"•";color:var(--blue);margin-right:10px}
.c-row{display:flex;gap:14px;font-size:15px;line-height:20px;margin-bottom:28px;color:var(--ink)}
.c-ico{flex:none;width:24px;height:24px;border:1.5px solid var(--blue);border-radius:6px;display:flex;align-items:center;justify-content:center}
.news-in{width:250px;height:40px;background:var(--white);border:1px solid #dfe4ea;margin-top:22px}
.news-btn{width:125px;height:36px;background:var(--blue);color:var(--white);font-size:13px;display:flex;align-items:center;justify-content:center;margin-top:14px}
.bar{top:4680px;height:59px;background:var(--blue);color:var(--white);font-size:13px}
.social{display:flex;gap:8px;position:absolute;right:86px;top:12px}
.social span{width:34px;height:34px;border-radius:50%;background:var(--white);opacity:.9}
</style>
</head>
<body>

<header class="hero">
  <svg class="abs" style="left:0;top:0" width="1200" height="677"><polygon points="1200,0 1200,561 755,561" fill="#0a6cc2"/><polygon points="110,677 1200,677 1200,640 140,640" fill="#dfe6ee"/></svg>
  <div class="abs brand-badge">Marrowgate Concepts LLC</div>
  <nav class="nav"><span class="active">Home</span><span>About Us</span><span>Services</span><span>Testimonials</span></nav>
  <div class="abs nav-cta">Contact Us</div>
  <div class="abs hero-welcome">Welcome to Our</div>
  <div class="abs hero-title">Marrowgate<br>Concepts LLC</div>
  <div class="btn" style="left:86px;top:438px;width:167px;height:59px">Find Out More</div>
  <div class="placeholder" role="img" aria-label="Photo of a consultant in a dark suit working on a laptop" style="left:462px;top:305px;width:318px;height:372px;background:linear-gradient(160deg,#5a5f66,#2a2d31);border-radius:120px 120px 0 0"></div>
</header>

<section class="about">
  <svg class="abs" style="left:0;top:0" width="1200" height="652"><polygon points="86,306 86,601 378,601 358,582 108,582 108,306" fill="#0a6cc2"/></svg>
  <div class="placeholder" role="img" aria-label="Photo of three businesswomen reviewing work at an office desk" style="left:109px;top:124px;width:385px;height:458px;background:linear-gradient(135deg,#5b4a3d,#2c241e 60%,#8b7a6a)"></div>
  <div class="abs" style="left:604px;top:122px;font-size:20px;font-weight:500">Who We Are</div>
  <div class="abs title" style="left:604px;top:146px;text-align:left">About US</div>
  <p class="abs about-copy">Lorem ipsum dolor sit amet, consectetur adipiscing elit, sed do eiusmod tempor incididunt ut labore et dolore magna aliqua. Ut enim ad minim veniam, quis nostrud exercitation ullamco laboris nisi ut aliquip ex ea commodo consequat. Duis aute irure dolor in reprehenderit in voluptate velit esse cillum dolore eu fugiat nulla pariatur. Excepteur sint occaecat cupidatat non proident, sunt in culpa qui officia .</p>
  <div class="btn" style="left:604px;top:471px;width:158px;height:63px">READ MORE</div>
</section>

<section class="services">
  <svg class="abs" style="left:0;top:0" width="1200" height="988">
    <polygon points="0,80 0,0 0,0 500,530 0,530" fill="#ffffff" opacity=".55"/>
    <polygon points="1200,557 1200,988 791,988" fill="#0a6cc2"/>
    <rect x="786" y="236" width="328" height="340" fill="#fff"/>
    <line x1="436" y1="236" x2="436" y2="933" stroke="#cfd6de" stroke-dasharray="3 3"/>
    <line x1="786" y1="236" x2="786" y2="933" stroke="#cfd6de" stroke-dasharray="3 3"/>
    <line x1="86" y1="576" x2="786" y2="576" stroke="#cfd6de" stroke-dasharray="3 3"/>
  </svg>
  <div class="abs eyebrow" style="left:0;width:1200px;top:104px">What We Do</div>
  <div class="abs title" style="left:0;width:1200px;top:130px">Our Services</div>

  <div class="svc" style="left:73px;top:278px">
    <div class="svc-icon"><svg width="44" height="44" viewBox="0 0 44 44"><circle cx="22" cy="20" r="15" fill="#0a6cc2"/><rect x="14" y="30" width="12" height="10" fill="#0a6cc2"/><circle cx="22" cy="19" r="5" fill="#fff"/></svg></div>
    <h3>Lorem ipsum dolor</h3>
    <p>Lorem ipsum dolor sit amet, con secte tur adipiscing elit. Morbi libero justo, condimentum vitae varius ac, aliquam condimentum sapien.</p>
  </div>
  <div class="svc" style="left:425px;top:278px">
    <div class="svc-icon"><svg width="44" height="44" viewBox="0 0 44 44"><rect x="5" y="8" width="34" height="22" rx="2" fill="none" stroke="#0a6cc2" stroke-width="3"/><rect x="18" y="30" width="8" height="6" fill="#0a6cc2"/><rect x="13" y="36" width="18" height="3" fill="#0a6cc2"/></svg></div>
    <h3>Lorem ipsum dolor</h3>
    <p>Lorem ipsum dolor sit amet, con secte tur adipiscing elit. Morbi libero justo, condimentum vitae varius ac, aliquam condimentum sapien.</p>
  </div>
  <div class="svc" style="left:777px;top:278px">
    <div class="svc-icon"><svg width="44" height="44" viewBox="0 0 44 44"><circle cx="22" cy="20" r="9" fill="#0a6cc2"/><rect x="18" y="29" width="8" height="7" fill="#0a6cc2"/><g stroke="#0a6cc2" stroke-width="2"><line x1="22" y1="3" x2="22" y2="7"/><line x1="6" y1="20" x2="10" y2="20"/><line x1="34" y1="20" x2="38" y2="20"/><line x1="10" y1="8" x2="13" y2="11"/><line x1="34" y1="8" x2="31" y2="11"/></g></svg></div>
    <h3>Lorem ipsum dolor</h3>
    <p>Lorem ipsum dolor sit amet, con secte tur adipiscing elit. Morbi libero justo, condimentum vitae varius ac, aliquam condimentum sapien.</p>
  </div>
  <div class="svc" style="left:73px;top:646px">
    <div class="svc-icon"><svg width="44" height="44" viewBox="0 0 44 44"><circle cx="20" cy="20" r="14" fill="none" stroke="#0a6cc2" stroke-width="3"/><ellipse cx="20" cy="20" rx="6" ry="14" fill="none" stroke="#0a6cc2" stroke-width="2"/><line x1="6" y1="20" x2="34" y2="20" stroke="#0a6cc2" stroke-width="2"/><rect x="26" y="26" width="12" height="14" rx="4" fill="#0a6cc2"/></svg></div>
    <h3>Lorem ipsum dolor</h3>
    <p>Lorem ipsum dolor sit amet, con secte tur adipiscing elit. Morbi libero justo, condimentum vitae varius ac, aliquam condimentum sapien.</p>
  </div>
  <div class="svc" style="left:425px;top:646px">
    <div class="svc-icon"><svg width="44" height="44" viewBox="0 0 44 44"><polyline points="6,6 6,38 40,38" fill="none" stroke="#0a6cc2" stroke-width="2"/><rect x="11" y="26" width="5" height="10" fill="#0a6cc2"/><rect x="19" y="20" width="5" height="16" fill="#0a6cc2"/><rect x="27" y="24" width="5" height="12" fill="#0a6cc2"/><rect x="34" y="14" width="5" height="22" fill="#0a6cc2"/></svg></div>
    <h3>Lorem ipsum dolor</h3>
    <p>Lorem ipsum dolor sit amet, con secte tur adipiscing elit. Morbi libero justo, condimentum vitae varius ac, aliquam condimentum sapien.</p>
  </div>
</section>

<section class="why">
  <div class="abs eyebrow" style="left:0;width:1200px;top:74px">Marrowgate Concepts</div>
  <div class="abs title" style="left:0;width:1200px;top:100px">Why Choose Us</div>
  <p class="abs why-lead">Lorem ipsum dolor sit amet, consectetur adipiscing elit. Morbi libero<br>justo, condimentum vitae varius ac, aliquam condimentum sapien.</p>
  <div class="why-item" style="left:216px"><div class="why-box"><div><svg width="40" height="34" viewBox="0 0 40 34"><circle cx="20" cy="9" r="6" fill="#fff"/><circle cx="8" cy="12" r="4" fill="#fff"/><circle cx="32" cy="12" r="4" fill="#fff"/><path d="M9 30a11 11 0 0 1 22 0z" fill="#fff"/><path d="M0 30a8 8 0 0 1 10-7v7zM40 30a8 8 0 0 0-10-7v7z" fill="#fff"/></svg></div></div><span>Lorem ipsum dolor</span></div>
  <div class="why-item" style="left:407px"><div class="why-box"><div><svg width="40" height="36" viewBox="0 0 40 36"><rect x="3" y="6" width="26" height="24" fill="none" stroke="#fff" stroke-width="2.5"/><line x1="3" y1="13" x2="29" y2="13" stroke="#fff" stroke-width="2.5"/><circle cx="30" cy="27" r="7" fill="#fff"/><path d="M30 23v8M26 27h8" stroke="#0a6cc2" stroke-width="2"/></svg></div></div><span>Lorem ipsum dolor</span></div>
  <div class="why-item" style="left:606px"><div class="why-box"><div><svg width="40" height="36" viewBox="0 0 40 36" fill="none" stroke="#fff" stroke-width="2.5"><rect x="15" y="3" width="10" height="8"/><path d="M20 11v7M6 18h28M6 18v8M20 18v8M34 18v8"/><rect x="2" y="26" width="8" height="7"/><rect x="16" y="26" width="8" height="7"/><rect x="30" y="26" width="8" height="7"/></svg></div></div><span>Lorem ipsum dolor</span></div>
  <div class="why-item" style="left:803px"><div class="why-box"><div><svg width="40" height="36" viewBox="0 0 40 36" fill="none" stroke="#fff" stroke-width="2.5"><rect x="3" y="4" width="34" height="22"/><path d="M20 26v6M12 33h16"/><circle cx="14" cy="15" r="4"/><path d="M22 13h10M22 18h8"/></svg></div></div><span>Lorem ipsum dolor</span></div>
</section>

<section class="testimonials">
  <svg class="abs" style="left:0;top:0" width="1200" height="821"><polygon points="0,0 401,0 0,298" fill="#0a6cc2"/><polygon points="1200,560 1200,821 830,821" fill="#f2f7fd"/></svg>
  <div class="abs eyebrow" style="left:0;width:1200px;top:114px">Testimonials</div>
  <div class="abs title" style="left:0;width:1200px;top:150px">Our Happy Clients</div>
  <p class="abs t-lead">Lorem ipsum dolor sit amet, consectetur adipiscing elit. Morbi libero justo, condimentum vitae varius ac, aliquam condimentum sapien. Ut mi erat, venenatis dignissim auctor ut, accumsan cursus nisi.</p>

  <svg class="abs" style="left:40px;top:500px" width="28" height="44"><polyline points="24,2 4,22 24,42" fill="none" stroke="#555" stroke-width="3"/></svg>
  <svg class="abs" style="left:1134px;top:500px" width="28" height="44"><polyline points="4,2 24,22 4,42" fill="none" stroke="#555" stroke-width="3"/></svg>

  <div class="t-card" style="left:86px"><div class="avatar" role="img" aria-label="Client portrait"></div>Lorem ipsum dolor sit amet, con secte tur adipiscing elit. Pellen tesque aliquet eros vitae placerat Lorem ipsum dolor sit amet, con sectetur adipiscing elit</div>
  <div class="t-card" style="left:434px"><div class="avatar" role="img" aria-label="Client portrait"></div>Lorem ipsum dolor sit amet, con secte tur adipiscing elit. Pellen tesque aliquet eros vitae placerat Lorem ipsum dolor sit amet, con sectetur adipiscing elit</div>
  <div class="t-card" style="left:782px"><div class="avatar" role="img" aria-label="Client portrait"></div>Lorem ipsum dolor sit amet, con secte tur adipiscing elit. Pellen tesque aliquet eros vitae placerat Lorem ipsum dolor sit amet, con sectetur adipiscing elit</div>

  <div class="t-meta" style="left:86px"><b>Lorem ipsum sit</b><small>Lorem ipsum</small><div class="stars"><svg width="104" height="18" viewBox="0 0 104 18"><g fill="#f7931e"><path id="st" d="M9 0l2.6 6 6.4.5-4.9 4.2 1.5 6.3L9 13.6 3.4 17l1.5-6.3L0 6.5 6.4 6z"/><use href="#st" x="21"/><use href="#st" x="42"/><use href="#st" x="63"/><use href="#st" x="84"/></g></svg></div></div>
  <div class="t-meta" style="left:434px"><b>Lorem ipsum sit</b><small>Lorem ipsum</small><div class="stars"><svg width="104" height="18" viewBox="0 0 104 18"><g fill="#f7931e"><use href="#st"/><use href="#st" x="21"/><use href="#st" x="42"/><use href="#st" x="63"/><use href="#st" x="84"/></g></svg></div></div>
  <div class="t-meta" style="left:782px"><b>Lorem ipsum sit</b><small>Lorem ipsum</small><div class="stars"><svg width="104" height="18" viewBox="0 0 104 18"><g fill="#f7931e"><use href="#st"/><use href="#st" x="21"/><use href="#st" x="42"/><use href="#st" x="63"/><use href="#st" x="84"/></g></svg></div></div>
</section>

<section class="contact">
  <svg class="abs" style="left:0;top:0" width="1200" height="725"><polygon points="1200,508 1200,725 898,725" fill="#0a6cc2"/></svg>
  <div class="abs eyebrow" style="left:0;width:1200px;top:98px">Contact Us</div>
  <div class="abs title" style="left:0;width:1200px;top:128px">How Can We Help You</div>
  <div class="field" style="left:86px;top:241px;width:507px;height:66px"><svg width="14" height="16"><circle cx="7" cy="4" r="4" fill="#666"/><path d="M0 16a7 7 0 0 1 14 0z" fill="#666"/></svg>First Name</div>
  <div class="field" style="left:605px;top:241px;width:509px;height:66px"><svg width="18" height="13"><rect x="0.5" y="0.5" width="17" height="12" fill="#666"/><polyline points="1,1 9,7 17,1" fill="none" stroke="#fff"/></svg>E-Mail</div>
  <div class="field" style="left:86px;top:337px;width:507px;height:66px"><svg width="12" height="17"><rect x="1" y="1" width="10" height="15" rx="2" fill="none" stroke="#666" stroke-width="2"/></svg>Phone Number</div>
  <div class="field" style="left:605px;top:337px;width:509px;height:66px"><svg width="12" height="16"><path d="M6 0a6 6 0 0 1 6 6c0 4-6 10-6 10S0 10 0 6a6 6 0 0 1 6-6z" fill="#666"/><circle cx="6" cy="6" r="2" fill="#fff"/></svg>Address</div>
  <div class="field msg" style="left:86px;top:436px;width:1028px;height:129px"><svg width="16" height="16"><circle cx="8" cy="8" r="8" fill="#666"/><circle cx="5" cy="8" r="1.2" fill="#fff"/><circle cx="8" cy="8" r="1.2" fill="#fff"/><circle cx="11" cy="8" r="1.2" fill="#fff"/></svg>Message</div>
  <div class="btn" style="left:493px;top:598px;width:219px;height:59px;border-radius:10px">SUBMIT NOW</div>
</section>

<footer class="footer">
  <div class="abs f-brand"><div style="width:30px;height:30px;background:var(--blue);margin:0 auto 12px"></div>Marrowgate Concepts LLC</div>
  <div class="abs f-col" style="left:375px;top:68px"><h4>QUICK LINKS</h4><ul><li>Home</li><li>About Us</li><li>Services</li><li>Testimonials</li><li>Contact Us</li></ul></div>
  <div class="abs f-col" style="left:565px;top:68px;width:260px"><h4>CONTACT US</h4>
    <div style="margin-top:28px">
      <div class="c-row"><span class="c-ico"><svg width="10" height="13"><path d="M5 0a5 5 0 0 1 5 5c0 3-5 8-5 8S0 8 0 5a5 5 0 0 1 5-5z" fill="#0a6cc2"/></svg></span><span>Address Line here Dummy<br>Address Line here</span></div>
      <div class="c-row"><span class="c-ico"><svg width="12" height="12"><path d="M2 1l3 0 1 3-2 1a7 7 0 0 0 3 3l1-2 3 1v3c-6 0-10-4-10-9z" fill="#0a6cc2"/></svg></span><span>+012 345 6789</span></div>
      <div class="c-row"><span class="c-ico"><svg width="12" height="9"><rect width="12" height="9" fill="#0a6cc2"/><polyline points="0,0 6,5 12,0" fill="none" stroke="#fff"/></svg></span><span>hello@marrowgateconcepts.com</span></div>
    </div>
  </div>
  <div class="abs f-col" style="left:867px;top:68px;width:260px"><h4>OUR NEWSLETTER</h4>
    <p style="font-size:15px;line-height:20px;margin-top:28px">Subscribe our newsletter to get the latest news.</p>
    <div class="news-in"></div>
    <div class="news-btn">SUBSCRIBE</div>
  </div>
</footer>

<div class="abs bar" style="left:0;width:1200px">
  <span class="abs" style="left:86px;top:20px">Copyright © 2023 All Rights Reserved By Marrowgate Concepts LLC.</span>
  <div class="social"><span></span><span></span><span></span><span></span></div>
</div>

</body>
</html>
```